Delvin & Associates - London New Letting and Property Management Company *

Delvin & Associates LTD is a new company based in London, and works with brand new residential property in the city centre.

We are aiming to have 1000 new properties a year.

We are looking for something modern and minimalistic :
Logo ,Monogram, Paper Head and Business Card.

Target Market(s)

Internation landlords

Industry/Entity Type

Real Estate

Logo Text

Delvin & Associates

Colors

Designer to choose colors to be used in the design.

Requirements
Nice to have
• A particular monogram with "DA"
Should not have
• Little House over the logo

```html
<!DOCTYPE html>
<html lang="en">
<head>
<meta charset="utf-8">
<title>Delvin &amp; Associates – Stationery</title>
<link href="https://fonts.googleapis.com/css2?family=Barlow:wght@400;500&family=Montserrat:wght@400;500&display=swap" rel="stylesheet">
<style>
  :root{
    --brand-blue:#0655a3;
    --brand-green:#7dc03b;
    --ink:#2b2b2b;
    --paper:#ffffff;
    --backdrop:#e9ebeb;
    --signature:#d9dee4;
  }
  *{margin:0;padding:0;box-sizing:border-box}
  html,body{width:1200px;height:1000px;overflow:hidden;background:var(--backdrop)}
  body{position:relative;font-family:"Barlow",Arial,sans-serif;color:var(--ink)}

  .brand{display:flex;flex-direction:column;align-items:center;text-align:center;line-height:1}
  .brand__mark{background:var(--brand-green);margin-bottom:6px}
  .brand__name{font-family:"Barlow",Arial,sans-serif;font-weight:500;color:var(--brand-blue);white-space:nowrap}
  .brand__tag{font-family:"Barlow",Arial,sans-serif;font-weight:500;color:var(--brand-green);letter-spacing:.2em;white-space:nowrap;margin-top:3px}

  /* business card front */
  .card-front{position:absolute;left:100px;top:87px;width:237px;height:135px;background:var(--brand-blue);display:flex;align-items:center;justify-content:center}
  .card-front .brand__mark{width:18px;height:18px}
  .card-front .brand__name{color:#fff;font-size:17px}
  .card-front .brand__tag{font-size:7px}

  /* business card back */
  .card-back{position:absolute;left:366px;top:87px;width:235px;height:135px;background:var(--paper);overflow:hidden}
  .card-back .brand{position:absolute;left:9px;top:10px}
  .card-back .brand__mark{width:14px;height:14px;margin-bottom:4px}
  .card-back .brand__name{font-size:13px}
  .card-back .brand__tag{font-size:5.5px}
  .card-holder{position:absolute;right:10px;top:10px;text-align:right;line-height:1}
  .card-holder__name{font-size:11px;font-weight:500;color:var(--brand-blue)}
  .card-holder__role{font-size:7px;color:var(--brand-green);margin-top:1px}
  .card-back .contacts{position:absolute;left:9px;top:79px;font-size:7px}
  .card-back .contacts li{height:10px}
  .card-back .contacts svg{width:7px;height:7px}
  .card-back .band{position:absolute;left:0;bottom:0;width:100%;height:9px}

  .contacts{list-style:none;font-family:"Montserrat",Arial,sans-serif;font-weight:500;color:var(--brand-blue)}
  .contacts li{display:flex;align-items:center;gap:4px}
  .contacts svg{flex:none;fill:var(--brand-green)}

  /* letterhead */
  .letterhead{position:absolute;left:100px;top:271px;width:463px;height:629px;background:var(--paper);overflow:hidden}
  .letterhead .brand{position:absolute;left:0;right:0;top:50px}
  .letterhead .brand__mark{width:22px;height:22px}
  .letterhead .brand__name{font-size:20px}
  .letterhead .brand__tag{font-size:9px}
  .letter{position:absolute;left:51px;top:160px;width:343px;font-family:"Montserrat",Arial,sans-serif;font-size:8.6px;line-height:12.4px;color:var(--ink)}
  .letter__greeting{font-size:11px;margin-bottom:25px}
  .letter__body{text-align:justify;margin-bottom:12px}
  .letter__sender{margin-top:20px}
  .letter__sender-name{font-size:11px}
  .letter__sender-role{font-size:7px}
  .signature{position:absolute;left:40px;top:510px;width:92px;height:42px;background:var(--signature);border-radius:4px}
  .letterhead .contacts{position:absolute;left:297px;top:559px;font-size:8.5px}
  .letterhead .contacts li{height:12.3px}
  .letterhead .contacts svg{width:8px;height:8px}
  .letterhead .band{position:absolute;left:0;bottom:0;width:100%;height:12px}

  /* presentation folder */
  .folder{position:absolute;left:636px;top:270px;width:464px;height:631px}
  .folder__shape{position:absolute;inset:0}
  .folder .brand{position:absolute;left:0;width:462px;top:218px}
  .folder .brand__mark{width:54px;height:54px;margin-bottom:14px}
  .folder .brand__name{color:#fff;font-size:36px}
  .folder .brand__tag{font-size:16px;margin-top:7px}
</style>
</head>
<body>

<section class="card-front" aria-label="Business card, front">
  <div class="brand">
    <span class="brand__mark" style="margin-bottom:5px"></span>
    <span class="brand__name">Delvin &amp; Associates</span>
    <span class="brand__tag">PROPERTY MANAGEMENT</span>
  </div>
</section>

<section class="card-back" aria-label="Business card, back">
  <div class="brand">
    <span class="brand__mark"></span>
    <span class="brand__name">Delvin &amp; Associates</span>
    <span class="brand__tag">PROPERTY MANAGEMENT</span>
  </div>
  <div class="card-holder">
    <div class="card-holder__name">Alan Grey</div>
    <div class="card-holder__role">Owner</div>
  </div>
  <ul class="contacts">
    <li><svg viewBox="0 0 10 10"><path d="M2 1h2l1 2-1 1a5 5 0 0 0 2 2l1-1 2 1v2c-4 0-7-3-7-7z"/></svg>020 555 0148</li>
    <li><svg viewBox="0 0 10 10"><rect x="3" y="0.5" width="4.5" height="9" rx="1"/></svg>020 555 0148</li>
    <li><svg viewBox="0 0 10 10"><path d="M0 2h10v6H0z"/></svg>office@delvin-associates.com</li>
    <li><svg viewBox="0 0 10 10"><circle cx="5" cy="5" r="4.5"/></svg>delvin-associates.com</li>
  </ul>
  <svg class="band" viewBox="0 0 235 9" preserveAspectRatio="none">
    <polygon points="0,0 160,0 168,9 0,9" fill="var(--brand-green)"/>
    <polygon points="163,4 235,4 235,9 168,9" fill="var(--brand-blue)"/>
  </svg>
</section>

<section class="letterhead" aria-label="Letterhead">
  <div class="brand">
    <span class="brand__mark"></span>
    <span class="brand__name">Delvin &amp; Associates</span>
    <span class="brand__tag">PROPERTY MANAGEMENT</span>
  </div>
  <div class="letter">
    <p class="letter__greeting">Dear Mr. Hart,</p>
    <p class="letter__body">Lorem ipsum dolor sit amet, consectetur adipiscing elit. Donec orci purus, luctus vitae dignissim eu, iaculis sed purus. Vivamus faucibus, ipsum nec aliquet viverra, leo mauris condimentum ligula, sit amet sagittis enim ligula quis arcu. Nam egestas tortor id nisi porttitor mattis. In tortor ante, ultricies in suscipit a, tempus non massa. Vivamus et auctor mi. Fusce vel massa nulla. Phasellus nec eros mauris, et scelerisque orci. Donec malesuada orci vitae nulla accumsan porta a id massa. Quisque accumsan iaculis magna sit amet fringilla. Maecenas consequat, magna eget tincidunt semper, odio nibh rutrum mi, id feugiat ante nisi eu risus. Vestibulum nunc orci, rhoncus a placerat in, ultricies in mi. Cras mattis varius eros, vel fringilla nisi suscipit eget.</p>
    <p class="letter__body">Quisque scelerisque sagittis nulla at porttitor. Mauris a justo et tellus interdum tristique. Sed id augue vitae urna euismod commodo aliquet a quam. Pellentesque arcu velit, cursus et malesuada ut, consequat et diam. Nullam erat sem, rhoncus id ullamcorper vitae, rhoncus et arcu. In ultricies ultricies nulla, ut rutrum nisi iaculis at. Donec eu magna a metus ornare faucibus. Fusce aliquet faucibus ultricies. Morbi semper, est id tincidunt gravida, sem arcu adipiscing lacus, ac bibendum nulla leo eu purus. Quisque nec diam sed risus consectetur a ccumsan quis nibh. Vestibulum id purus lorem.</p>
    <div class="letter__sender">
      <div class="letter__sender-name">Alan Grey</div>
      <div class="letter__sender-role">Co-Founder &amp; CEO</div>
    </div>
  </div>
  <div class="signature" role="img" aria-label="Handwritten signature of Alan Grey"></div>
  <ul class="contacts">
    <li><svg viewBox="0 0 10 10"><path d="M2 1h2l1 2-1 1a5 5 0 0 0 2 2l1-1 2 1v2c-4 0-7-3-7-7z"/></svg>020 555 0148</li>
    <li><svg viewBox="0 0 10 10"><rect x="3" y="0.5" width="4.5" height="9" rx="1"/></svg>020 555 0148</li>
    <li><svg viewBox="0 0 10 10"><path d="M0 2h10v6H0z"/></svg>office@delvin-associates.com</li>
    <li><svg viewBox="0 0 10 10"><circle cx="5" cy="5" r="4.5"/></svg>delvin-associates.com</li>
  </ul>
  <svg class="band" viewBox="0 0 463 12" preserveAspectRatio="none">
    <polygon points="0,0 285,0 300,12 0,12" fill="var(--brand-green)"/>
    <polygon points="290,5 463,0 463,12 300,12" fill="var(--brand-blue)"/>
  </svg>
</section>

<section class="folder" aria-label="Presentation folder">
  <svg class="folder__shape" viewBox="0 0 464 631">
    <path d="M12 0H452a12 12 0 0 1 12 12V128q0 14-12 18q-16 4-16 20V300q0 16 16 20q12 4 12 18V619a12 12 0 0 1-12 12H12A12 12 0 0 1 0 619V12A12 12 0 0 1 12 0z" fill="var(--brand-blue)"/>
  </svg>
  <div class="brand">
    <span class="brand__mark"></span>
    <span class="brand__name">Delvin &amp; Associates</span>
    <span class="brand__tag">PROPERTY MANAGEMENT</span>
  </div>
</section>

</body>
</html>
```